Graphic background for 10 Pull Up Banners

To produce a graphic background for a 100 cm wide by 200 cm high Pull-Up Display banner containing a Buddhist text in three languages: Tibetan, Mandarin and English. Please refer to uploaded file "Elements of Pull Up Banner". The design should be simple (not drawing attention away from the text). This design should then be varied for or extended to the next banner and so on until the 10th banner. When the banners are lined up, they should form a single design that is 1000 cm wide by 200 cm high.
An alternative way to look at the project is to produce a graphic background of 1000 cm width by 200 cm height that is then splitted into ten separate 100 cm wide by 200 cm high graphic to be used as background for 10 Buddhist texts (text 1, 2, 3, 4, 5, 6, 7, 8, 9a, 9b) on 10 Pull-Up Display Banners, the text in each banner being in the three languages mentioned earlier.
In either perspective, the design should be simple and not draw attention away from the texts. See uploaded PDF file "Examples.pdf"
For attendees at a Buddhist Event.

```html
<!DOCTYPE html>
<html lang="en">
<head>
<meta charset="utf-8">
<title>Ten Mistaking</title>
<link rel="stylesheet" href="https://fonts.googleapis.com/css2?family=Noto+Serif+Tibetan:wght@400&family=Noto+Serif+SC:wght@400;500&family=Tinos:wght@400&display=swap">
<style>
  :root {
    --page: #ffffff;
    --peach: #fbd3bd;
    --peach-light: #fde8dc;
    --mint: #bfe3dc;
    --teal: #9fd2cb;
    --ink: #1e1e1e;
    --ink-soft: #333333;
    --red: #ad1a20;
    --deity-a: #e7b4a8;
    --deity-b: #f6dcd3;
    --flame-a: #e8401c;
    --flame-b: #f7c21e;
  }
  * { margin: 0; padding: 0; box-sizing: border-box; }
  html, body { width: 1200px; height: 2203px; overflow: hidden; background: var(--page); }
  .canvas { position: relative; width: 1200px; height: 2203px; background: var(--page); }

  .banner {
    position: absolute; left: 91px; top: 85px; width: 1012px; height: 2020px;
    overflow: hidden;
    background:
      radial-gradient(circle at 88% 8%, rgba(255,255,255,0.55) 0 90px, transparent 180px),
      radial-gradient(circle at 78% 30%, rgba(255,255,255,0.35) 0 120px, transparent 220px),
      radial-gradient(circle at 92% 55%, rgba(255,255,255,0.35) 0 110px, transparent 200px),
      radial-gradient(circle at 12% 45%, rgba(255,255,255,0.30) 0 100px, transparent 200px),
      radial-gradient(ellipse at 0% 30%, var(--peach) 0%, transparent 60%),
      radial-gradient(ellipse at 10% 80%, var(--peach) 0%, transparent 55%),
      radial-gradient(ellipse at 100% 20%, var(--teal) 0%, transparent 60%),
      radial-gradient(ellipse at 100% 75%, var(--teal) 0%, transparent 60%),
      linear-gradient(100deg, var(--peach-light) 0%, #fbf3ee 45%, var(--mint) 100%);
  }

  .deity-art {
    position: absolute; left: 55px; top: 46px; width: 206px; height: 198px;
    border-radius: 50% 50% 8px 8px;
    background: radial-gradient(circle at 50% 40%, var(--deity-b), var(--deity-a));
    opacity: 0.85;
  }

  .title-zh {
    position: absolute; left: 318px; top: 80px;
    font-family: "Noto Serif SC", serif; font-weight: 500; font-size: 64px;
    color: var(--red); letter-spacing: 4px; line-height: 1;
  }
  .title-en {
    position: absolute; left: 311px; top: 153px;
    font-family: "Tinos", "Times New Roman", serif; font-size: 70px;
    color: var(--red); line-height: 1;
  }

  .verse-bo {
    position: absolute; left: 172px; top: 264px; list-style: none;
    font-family: "Noto Serif Tibetan", serif; font-size: 25px;
    color: var(--ink); line-height: 44.6px; white-space: nowrap;
  }

  .verse-zh {
    position: absolute; left: 172px; top: 794px; list-style: none;
    font-family: "Noto Serif SC", serif; font-size: 19px;
    color: var(--ink-soft); line-height: 28.5px;
  }
  .notes-zh {
    position: absolute; left: 205px; top: 1089px; list-style: none;
    font-family: "Noto Serif SC", serif; font-size: 19px;
    color: var(--ink-soft); line-height: 29px;
  }

  .verse-en {
    position: absolute; left: 169px; top: 1197px; width: 600px;
    font-family: "Tinos", "Times New Roman", serif; font-size: 19.5px;
    color: var(--ink); line-height: 25px;
  }
  .verse-en p { margin-bottom: 17px; }

  .flame-art {
    position: absolute; left: 654px; top: 1625px; width: 293px; height: 330px;
    border-radius: 50% 50% 48% 48% / 62% 62% 38% 38%;
    background: radial-gradient(circle at 50% 62%, var(--flame-b) 0 32%, var(--flame-a) 70%);
  }

  .dedication { position: absolute; left: 228px; top: 1775px; color: var(--red); }
  .dedication-bo { font-family: "Noto Serif Tibetan", serif; font-size: 21px; line-height: 40px; white-space: nowrap; }
  .dedication-zh { font-family: "Noto Serif SC", serif; font-size: 29px; line-height: 44px; }
  .dedication-en { font-family: "Tinos", "Times New Roman", serif; font-size: 25px; line-height: 40px; }
</style>
</head>
<body>
<main class="canvas">
  <section class="banner">
    <div class="deity-art" role="img" aria-label="Line illustration of a seated Buddhist deity on a lotus throne"></div>
    <h1 class="title-zh">十个误解</h1>
    <h2 class="title-en">Ten Mistaking</h2>

    <ol class="verse-bo" lang="bo">
      <li>དད་པ་དང་འདོད་པ་ལ་ནོར་ས་ཡོད།།</li>
      <li>བྱམས་སྙིང་རྗེ་དང་ཆགས་པ་ལ་ནོར་ས་ཡོད།།</li>
      <li>ཤེས་བྱ་གཞིས་ཀྱི་སྟོང་པ་དང་བློས་བྱས་ཀྱི་སྟོང་པ་ལ་ནོར་ས་ཡོད།།</li>
      <li>ཆོས་ཀྱི་དབྱིངས་དང་ཆད་ལྟ་ལ་ནོར་ས་ཡོད།།</li>
      <li>ཉམས་མྱོང་དང་རྟོགས་པ་ལ་ནོར་ས་ཡོད།།</li>
      <li>བཙུན་པ་དང་རྒྱལ་འཚོལ་ལ་ནོར་ས་ཡོད།།</li>
      <li>འཁྲུལ་ཞིག་དང་བདུད་ཕྱིར་ལ་ནོར་ས་ཡོད།།</li>
      <li>གྲུབ་ཐོབ་དང་ཐོག་པོ་ལ་ནོར་ས་ཡོད།།</li>
      <li>གཞན་དོན་བྱེད་པ་དང་རང་དོན་བྱེད་པ་ལ་ནོར་ས་ཡོད།།</li>
      <li>ཐབས་མཁས་པ་དང་གཡོ་སྒྲུ་ལ་ནོར་ས་ཡོད།།</li>
    </ol>

    <ol class="verse-zh" lang="zh">
      <li>信心与爱欲可能混淆，</li>
      <li>慈悲与贪执可能混淆，</li>
      <li>所知1本空与思维造作空性可能混淆，</li>
      <li>法界与断见2可能混淆，</li>
      <li>觉受与证悟可能混淆，</li>
      <li>尊者与神棍可能混淆，</li>
      <li>破惑与著魔可能混淆，</li>
      <li>成就者与骗子可能混淆，</li>
      <li>利他与自利可能混淆，</li>
      <li>方便善巧与谄媚哄骗可能混淆。</li>
    </ol>
    <ol class="notes-zh" lang="zh">
      <li>1. 所知：可以认识的外景。</li>
      <li>2. 断见：否定因果、前生、后世等说法的见解。</li>
    </ol>

    <div class="verse-en">
      <p>Desire can be mistaken for faith or devotion.</p>
      <p>Attachment can be mistaken for love and compassion.</p>
      <p>Conceptual emptiness can be mistaken for the emptiness of the nature of phenomena.</p>
      <p>Nihilism can be mistaken for the dharmadhatu.</p>
      <p>A meditative experience can be mistaken for realization.</p>
      <p>Outer religious practices can be mistaken for inner development of good qualities.</p>
      <p>A person in the grip of a demon can be mistaken for a person who has destroyed his own delusions.</p>
      <p>A charlatan can be mistaken for a siddha.</p>
      <p>An act to benefit yourself can be mistaken for an act to benefit others.</p>
      <p>Deviousness can be mistaken for skilful means.</p>
    </div>

    <div class="flame-art" role="img" aria-label="Ornamental red and yellow flame emblem with an auspicious symbol at its centre"></div>

    <div class="dedication">
      <p class="dedication-bo" lang="bo">སེམས་ཅན་མ་ལུས་སངས་རྒྱས་ཐོབ་པར་ཤོག</p>
      <p class="dedication-zh" lang="zh">愿诸有情共证佛果位。</p>
      <p class="dedication-en">May all attain Buddhahood together.</p>
    </div>
  </section>
</main>
</body>
</html>
```